Business Card Design for drone videography and photography

I have a Vexor Talon 3 drone. I am looking for a logo to somehow incorporate with my business name. I don't even know what is an appropriate font. I am most filming real estate homes. I want something simplistic and a logo that makes sense for the business that I'm in. xxxxxxxxxxxxxxxxxxxxxxxxxxxxxxxxxxxxxxxxxxxxxxxxxxxxxxxxxxxxxxxxxxxxxxxxxxxxxxxxxxxxxxxxxxxxxxxxxxxxxxxxxxxxxxxxxxxxxxxxxxxxxxxxxxxxxxxxxxxxxxxxxxxxxxxxxxxxxxxxxxxxxxxxxxxxxxxxxxxxxxxxxxxxxxxxxxxxxxxxxxxxxxxxxxxxxxxxxxxxxxxxxxxxxxxxxxxxxxxxxxxxxxxxxxxxxxxxxxxxxxxxxxxxxxxxxxxxxxxxxxxxxxxxxxxxxxxxxxxxxxxxxxxxxxxxxxxxxxxxxxxxxxxxxxxxxxxxxxxxxxxxxxxxxxxxxxxxxxxxxxxxxxxxxxxxxxxxxxxxxxxxxxxxxxxxxxxxxxxxxxxxxxxxxxxxxxxxxxxxxxxxxxxxxxxxxxxxxxxxxxxxxxxxxxxxxxxxxxxxxxxxxxxxxxxxxxxxxxxxxxxxxxxxxxxxxxxxxxxxxxxxxxxxxxxxxxxxxxxxxxxxxxxxxxxxxxxxxxxxxxxxxxxxxxxxxxxxxxxxxxxxxxxxxxxxxxxxxxxxxxxxxxxxxxxxxxxxxxxxxxxxxxxxxxxxxxxxxxxxxxxxxxxxxxxxxxxxxxxxxxxxxxxxxxxxxxxxxxxxxxxxxxxxxxxxxxxxxxxxxxxxxxxxxxxxxxxxxxxxxxxxxxxxxxxxxxxxxxxxxxxxxxxxxxxxxxxxxxxxxxxxxxxxxxxxxxxxxxxxxxxxxxxxxxxxxxxxxxxxxxxxxxxxxxxxxxxxxxxxxxxxxxxxxxxxxxxxxxxxxxxxxxxxxxxxxxxxxxxxxxxxxxxxxxxxxxxxxxxxxxxxxxxxxxxxxxxxxxxxxxxxxxxxxxxxxxxxxxxxxxxxxxxxxxxxxxxxxxxxxxxxxxxxxxxxxxxxxxxxxxxxxxxxxxxxxxxxxxxxxxxxxxxxxxxxxxxxxxxxxxxxxxxxxxxxxxxxxxxxxxxxxxxxxxxxxxxxxxxxxxxxxxxxxxxxxxxxxxxx

Target Market(s)

Real estate

Industry/Entity Type

Business

Contact Information for Business Card

BRANDT SKYVIEW STUDIO
Daniel Brandt
Owner/Operator

48305 Birch Way
Fenwick Falls MO 64218

314-720-4163
dbrandt@brandtskyviewstudio.example

NCQ Drone Certified
Insured
Section 333 Exempt
Halvo Wing Class Certified

Font styles to use
Other font styles liked:
• PUMP DEMI BOLD LET

Requirements
Must have
• Maybe have the certifications on the back??? The business card must be more serious than playful
Nice to have
• Possibly have the logo work itself into the business name?
Should not have
• nothing that looks like a "fun" business. I want this business card to look professional but also simplistic. I don't want a picture that I took from my drone as the background.

```html
<!DOCTYPE html>
<html lang="en">
<head>
<meta charset="utf-8">
<title>Brandt Skyview Studio – Business Card</title>
<link rel="stylesheet" href="https://fonts.googleapis.com/css2?family=Jost:wght@300;400;600&display=swap">
<style>
  :root {
    --page: #ebe8e3;
    --card: #ffffff;
    --ink: #1c1c1c;
    --grey: #5b5b5b;
    --sky: #5aaed6;
    --frame: #2c86b4;
    --frame-dark: #1f6f99;
    --shadow: rgba(0, 0, 0, 0.18);
  }
  * { box-sizing: border-box; margin: 0; padding: 0; }
  html, body {
    width: 720px;
    height: 1200px;
    overflow: hidden;
    background: var(--page);
    font-family: "Jost", "Futura", sans-serif;
  }
  .sheet {
    width: 720px;
    height: 1200px;
    display: flex;
    flex-direction: column;
    align-items: center;
    justify-content: center;
    gap: 110px;
  }
  .card {
    position: relative;
    width: 600px;
    height: 343px;
    background: var(--card);
    box-shadow: 0 6px 18px var(--shadow);
  }

  /* Front side */
  .card-front .brand {
    position: absolute;
    top: 58px;
    right: 52px;
    display: flex;
    align-items: center;
    gap: 14px;
  }
  .brand-mark {
    width: 16px;
    height: 16px;
    border-radius: 50%;
    background: var(--sky);
    flex: none;
  }
  .brand-name {
    font-weight: 600;
    font-size: 24px;
    letter-spacing: 3px;
    line-height: 1;
    color: var(--ink);
    white-space: nowrap;
  }
  .contact {
    position: absolute;
    left: 54px;
    bottom: 40px;
  }
  .contact-name {
    font-weight: 300;
    font-size: 30px;
    color: var(--grey);
    line-height: 1.1;
  }
  .contact-role {
    font-weight: 300;
    font-size: 17px;
    color: var(--sky);
    margin-bottom: 14px;
  }
  .contact-line {
    display: flex;
    align-items: flex-start;
    gap: 12px;
    font-weight: 300;
    font-size: 16px;
    color: var(--grey);
    line-height: 1.4;
    margin-top: 6px;
    white-space: nowrap;
  }
  .contact-line svg {
    width: 13px;
    height: 13px;
    margin-top: 4px;
    flex: none;
    fill: var(--sky);
  }

  /* Back side */
  .card-back {
    background: linear-gradient(135deg, var(--frame), var(--frame-dark));
    padding: 22px;
  }
  .back-panel {
    position: relative;
    width: 100%;
    height: 100%;
    background: var(--card);
    display: flex;
    align-items: center;
    justify-content: center;
  }
  .back-panel .brand {
    display: flex;
    align-items: center;
    gap: 16px;
  }
  .back-panel .brand-name { font-size: 30px; letter-spacing: 4px; }
  .back-panel .brand-mark { width: 20px; height: 20px; }
  .cert-seal {
    position: absolute;
    top: 22px;
    right: 26px;
    width: 58px;
    height: 58px;
    border-radius: 50%;
    background: var(--sky);
    opacity: 0.75;
  }
</style>
</head>
<body>
<main class="sheet">

  <section class="card card-front" aria-label="Card front">
    <div class="brand">
      <span class="brand-mark"></span>
      <span class="brand-name">BRANDT SKYVIEW STUDIO</span>
    </div>

    <div class="contact">
      <p class="contact-name">Daniel Brandt</p>
      <p class="contact-role">Owner/Operator</p>
      <p class="contact-line">
        <svg viewBox="0 0 12 12" aria-hidden="true"><path d="M6 0a4 4 0 0 0-4 4c0 3 4 8 4 8s4-5 4-8a4 4 0 0 0-4-4zm0 5.6A1.6 1.6 0 1 1 6 2.4a1.6 1.6 0 0 1 0 3.2z"/></svg>
        <span>48305 Birch Way<br>Fenwick Falls MO 64218</span>
      </p>
      <p class="contact-line">
        <svg viewBox="0 0 12 12" aria-hidden="true"><path d="M0 1.5A1.5 1.5 0 0 1 1.5 0h9A1.5 1.5 0 0 1 12 1.5v9a1.5 1.5 0 0 1-1.5 1.5h-9A1.5 1.5 0 0 1 0 10.5zM3 2.5c-.5 0-.8.4-.7.9.5 3 2.3 4.9 5.3 5.6.5.1.9-.2.9-.7V7l-1.7-.6-.7.8C5 6.7 4.5 6 4.1 5.1l.8-.7L4.4 2.5z" fill-rule="evenodd"/></svg>
        <span>314-720-4163</span>
      </p>
      <p class="contact-line">
        <svg viewBox="0 0 12 12" aria-hidden="true"><path d="M0 2h12v8H0zm1 1.2V9h10V3.2L6 6.6z"/></svg>
        <span>dbrandt@brandtskyviewstudio.example</span>
      </p>
    </div>
  </section>

  <section class="card card-back" aria-label="Card back">
    <div class="back-panel">
      <span class="cert-seal" role="img" aria-label="Certification seal"></span>
      <div class="brand">
        <span class="brand-mark"></span>
        <span class="brand-name">BRANDT SKYVIEW STUDIO</span>
      </div>
    </div>
  </section>

</main>
</body>
</html>
```